Velvet Lantern Product Box

We are looking for a complete box design (box dimensions 9 in x 6 in x 3 in) for a new product that will be part of a subscription service. The concept is honey as the theme of a date night kit. It is a play on words, Honeymoon date night filled with Honey products. The company name is Copperleaf & Plum and we've provided logo images. There should be a sub-tag that will be on the box. Right now the tagline reads "Explore a more playful conscious way to love" (however, that tag line will change over the next couple of weeks).

Color palette should be more in the darker amber than yellow palette.

Web site for the book we are publishing is www.tendingkindreds.com

Please review box images that have been uploaded:
glint-box : interesting design on the inside of the box. Design all around the box
tru-pep-joy box: interesting use of logo on inside top of box
glint box: great use of color all around box exterior with complementary color on the inside
velvet-under box: fun use of word on box top. Good use of fun color on inside of box bottom
lumen box: good use of contrasting color on inside of box
ah-willow box: good use of words all around the box. Fun use of color and imagery inside the box
lisse-doral box: good use of words around the edges

Target Market(s)

Couples interested in date night kits

Industry/Entity Type

Education

Font styles to use
Serif

Colors
faa54b
fbca95
f68e4e

Requirements
Must have
• Must have completely box design compatible with Boxwright (https://boxwright.com/products/mailer-box). Amber color and honey theme.
• Box must have printing on all sides and on the interior.
Nice to have
• Swirls that represent the Copperleaf components of the name
Should not have
• Stay away from bees, images of honeycombs, bee hives.

```html
<!DOCTYPE html>
<html lang="en">
<head>
<meta charset="utf-8">
<title>Velvet Lantern Product Box – Dieline</title>
<link rel="stylesheet" href="https://fonts.googleapis.com/css2?family=Dancing+Script:wght@500;600&display=swap">
<style>
  :root {
    --page-bg: #f1f2f2;
    --plum-navy: #383751;
    --amber-deep: #6e3800;
    --amber-bright: #ee9000;
    --honey-gold: #f7d595;
    --gold-strong: rgba(250, 205, 120, 0.62);
    --gold-mid: rgba(250, 205, 120, 0.34);
    --gold-none: rgba(250, 205, 120, 0);
    --heart-red: rgba(214, 52, 98, 0.85);
    --heart-pink: rgba(232, 120, 160, 0.6);
    --heart-none: rgba(232, 120, 160, 0);
    --ink: #1d1d1f;
    --script: "Dancing Script", cursive;
  }
  * { margin: 0; padding: 0; box-sizing: border-box; }
  html, body { width: 1200px; height: 2570px; overflow: hidden; }
  body { background: var(--page-bg); position: relative; font-family: var(--script); }

  .panel { position: absolute; background: var(--plum-navy); overflow: hidden; }
  .flap-top    { left: 279px; top: 118px; width: 634px; height: 202px; }
  .flap-left   { left: 75px;  top: 325px; width: 202px; height: 432px; }
  .flap-right  { left: 919px; top: 325px; width: 202px; height: 432px; }
  .lid         { left: 281px; top: 323px; width: 634px; height: 434px;
                 background: linear-gradient(90deg, var(--amber-deep), var(--amber-bright)); }
  .front-wall  { left: 281px; top: 760px; width: 634px; height: 202px; }
  .inside-panel{ left: 279px; top: 1072px; width: 634px; height: 431px; }

  /* gold foliage areas */
  .foliage { position: absolute; }
  .foliage-band {
    left: 0; top: 0; width: 100%; height: 130px;
    background: linear-gradient(180deg, var(--gold-strong), var(--gold-mid) 55%, var(--gold-none));
  }
  .foliage-drape-left {
    left: 0; top: 0; width: 190px; height: 290px;
    background: linear-gradient(180deg, var(--gold-strong), var(--gold-mid) 60%, var(--gold-none));
    clip-path: polygon(0 0, 100% 0, 70% 35%, 30% 70%, 10% 100%, 0 100%);
  }
  .foliage-drape-right {
    right: 0; top: 0; width: 190px; height: 290px;
    background: linear-gradient(180deg, var(--gold-strong), var(--gold-mid) 60%, var(--gold-none));
    clip-path: polygon(0 0, 100% 0, 100% 100%, 90% 100%, 70% 70%, 30% 35%);
  }
  .foliage-side {
    top: 0; left: 0; width: 100%; height: 290px;
    background: linear-gradient(180deg, var(--gold-strong), var(--gold-mid) 55%, var(--gold-none));
  }
  .flap-left .foliage-side  { clip-path: polygon(0 0, 100% 0, 100% 100%, 85% 100%, 40% 45%, 0 25%); }
  .flap-right .foliage-side { clip-path: polygon(0 0, 100% 0, 100% 25%, 60% 45%, 15% 100%, 0 100%); }
  .sprig-left {
    left: 4px; bottom: 0; width: 128px; height: 82px;
    background: linear-gradient(20deg, var(--gold-strong), var(--gold-none) 80%);
    clip-path: polygon(0 100%, 0 40%, 40% 10%, 100% 55%, 40% 70%, 10% 100%);
  }
  .sprig-right {
    right: 2px; top: 2px; width: 70px; height: 72px;
    background: linear-gradient(225deg, var(--gold-strong), var(--gold-none) 85%);
    clip-path: polygon(100% 0, 100% 40%, 20% 100%, 0 85%, 55% 0);
  }

  /* brand name */
  .brand-name { position: absolute; color: var(--honey-gold); font-family: var(--script);
    font-weight: 600; white-space: nowrap; line-height: 1; }
  .brand-name span { position: absolute; display: block; text-align: center; transform: translateX(-50%); }
  .lid .brand-name { left: 0; top: 0; width: 100%; height: 100%; font-size: 62px; }
  .lid .brand-name .w1 { left: 280px; top: 165px; }
  .lid .brand-name .amp { left: 272px; top: 238px; font-size: 40px; }
  .lid .brand-name .w2 { left: 270px; top: 285px; }

  .flap-top .brand-name { left: 0; top: 0; width: 100%; height: 100%; font-size: 38px;
    transform: rotate(180deg); }
  .flap-top .brand-name .w1 { left: 320px; top: 60px; }
  .flap-top .brand-name .amp { left: 325px; top: 100px; font-size: 24px; }
  .flap-top .brand-name .w2 { left: 330px; top: 126px; }

  .inside-panel .brand-name { left: 0; top: 0; width: 100%; height: 100%; font-size: 64px; }
  .inside-panel .brand-name .w1 { left: 325px; top: 150px; }
  .inside-panel .brand-name .amp { left: 318px; top: 225px; font-size: 40px; }
  .inside-panel .brand-name .w2 { left: 318px; top: 268px; }

  .tagline { position: absolute; left: 0; width: 100%; top: 76px; text-align: center;
    color: var(--honey-gold); font-family: var(--script); font-weight: 500; font-size: 29px; }
  .tagline svg { vertical-align: -2px; margin-left: 10px; }

  /* interior hearts */
  .heart-confetti { position: absolute; left: 0; top: 0; width: 100%; height: 100%;
    background:
      radial-gradient(ellipse 60% 40% at 50% 0%, var(--heart-red), var(--heart-none) 100%),
      linear-gradient(180deg, var(--heart-pink) 0%, rgba(232,120,160,0.45) 30%, rgba(232,120,160,0.12) 55%, var(--heart-none) 100%); }

  .section-label { position: absolute; left: 303px; top: 1030px; font-family: var(--script);
    font-weight: 500; font-size: 32px; color: var(--ink); line-height: 1; }
</style>
</head>
<body>

  <section class="panel flap-top" aria-label="Top tuck flap">
    <p class="brand-name"><span class="w1">Copperleaf</span><span class="amp">&amp;</span><span class="w2">Plum</span></p>
  </section>

  <section class="panel flap-left" aria-label="Left side wall">
    <div class="foliage foliage-side" role="img" aria-label="Gold line-art leaves and branches hanging from the top edge"></div>
  </section>

  <section class="panel lid" aria-label="Box lid">
    <div class="foliage foliage-band" role="img" aria-label="Gold line-art leaves and buds along the top edge"></div>
    <div class="foliage foliage-drape-left" role="img" aria-label="Gold line-art leaves trailing down the left side"></div>
    <div class="foliage foliage-drape-right" role="img" aria-label="Gold line-art leaves trailing down the right side"></div>
    <h1 class="brand-name"><span class="w1">Copperleaf</span><span class="amp">&amp;</span><span class="w2">Plum</span></h1>
  </section>

  <section class="panel flap-right" aria-label="Right side wall">
    <div class="foliage foliage-side" role="img" aria-label="Gold line-art leaves and branches hanging from the top edge"></div>
  </section>

  <section class="panel front-wall" aria-label="Front wall">
    <div class="foliage sprig-right" role="img" aria-label="Small gold flower sprig in the corner"></div>
    <div class="foliage sprig-left" role="img" aria-label="Small gold leaf sprig in the corner"></div>
    <p class="tagline">Explore a more playful conscious way to love<svg width="22" height="20" viewBox="0 0 22 20" aria-hidden="true"><path d="M11 18 C4 12 1 9 1 5.5 A4.5 4.5 0 0 1 11 4 A4.5 4.5 0 0 1 21 5.5 C21 9 18 12 11 18 Z" fill="none" stroke="#f7d595" stroke-width="1.6"/></svg></p>
  </section>

  <p class="section-label">inside</p>

  <section class="panel inside-panel" aria-label="Inside of lid">
    <div class="heart-confetti" role="img" aria-label="Scattered pink and red confetti hearts falling from the top and thinning out below"></div>
    <p class="brand-name"><span class="w1">Copperleaf</span><span class="amp">&amp;</span><span class="w2">Plum</span></p>
  </section>

</body>
</html>
```